organic collagen powder needs packaging design

We are about to start a company, that sells nutritional supplements online - especially on Brellow. For now we are in need of a packaging design for organic collagen powder (Types I, II and III) maybe including also elastin and eventually hyaluronic acid, which is going to be our first product. We are planning on developing organic nutritional supplements of any kind and this is our initial product. Our upscale products must commincate a solid value proposition, the easygoing solution of a real problem, be understandable by users, perform their task as easily and efficiently as possible, and become better and harder to part with the more they are used. To us it is of the utmost importance to produce and sell organic quality products, which are free of any preservatives, chemical fillers, economic extenders or any other unhealthy ingredients. We want our products to come across as high-quality ones (but in no way conservative or unadventurous), vivid, hip, friendly, reliable, modern and healthy. People - men and women alike - should generally be able to unmistakably connect any of our products immediately to our company and to our product line, so the product packaging should be maximally distinctive. Since we will also need further packaging design for further products in the future please consider that the packaging design is scalable for further products/product-line up. We are thinking about defining our products mainly through design as we are not exactly sure yet, if we want to have a brand name for the products. The products are supposed to address men and women, that are looking for healthy nutrition, that are eager to stay fit and in health and that have a modern view and attitude about life. Although our Collagen will not be vegan (the product itself will be of animal origin = hydrolysed bovine collagen), we basically strive for plant based and vegan nutritional supplements without any unnecessary additives.

Target Market(s)

Hip men and women, who want to stay healthy and fit and have an easygoing, modern attitude to life.

Industry/Entity Type

Nutritional supplements, organic (largely vegan products - when possible and reasonable)

Requirements
Must have
• Maximally distinctive design
Nice to have
• Design should be vivid and happy
Should not have
• simple black packaging with simple writing on it

```html
<!DOCTYPE html>
<html lang="en">
<head>
<meta charset="utf-8">
<title>Organic Collagen Powder – Packaging Label</title>
<link rel="stylesheet" href="https://fonts.googleapis.com/css2?family=Poppins:wght@200;300;400&family=Comfortaa:wght@700&family=Montserrat:wght@800&display=swap">
<style>
  :root {
    --teal: #77cabd;
    --forest: #0a4a35;
    --meadow: #72b77f;
    --grass: #41b97a;
    --ink: #333f3c;
    --paper: #ffffff;
  }
  * { margin: 0; padding: 0; box-sizing: border-box; }
  html, body { width: 1058px; height: 1200px; overflow: hidden; background: var(--paper); }
  .label {
    position: relative;
    width: 1058px;
    height: 1200px;
    overflow: hidden;
    background: var(--paper);
    font-family: "Poppins", sans-serif;
    color: var(--ink);
  }
  .side-art {
    position: absolute;
    top: 0;
    height: 1200px;
  }
  .side-art--left {
    left: 0;
    width: 176px;
    background: linear-gradient(180deg, var(--forest) 0%, #2f8a72 35%, var(--teal) 62%, var(--meadow) 80%, var(--teal) 100%);
  }
  .side-art--right {
    right: 0;
    width: 152px;
    background: linear-gradient(180deg, var(--teal) 0%, var(--forest) 30%, #2f8a72 55%, var(--grass) 75%, var(--forest) 100%);
  }
  .splash {
    position: absolute;
    background: var(--teal);
    opacity: 0.9;
  }
  .splash--top {
    left: 533px; top: 42px; width: 373px; height: 300px;
    border-radius: 48% 52% 40% 60% / 45% 40% 60% 55%;
  }
  .splash--mid {
    left: 176px; top: 693px; width: 152px; height: 88px;
    border-radius: 40% 60% 60% 40% / 50% 50% 50% 50%;
  }
  .leaf-corner {
    position: absolute;
    background: linear-gradient(160deg, var(--teal), #6bbfb1);
  }
  .leaf-corner--right {
    left: 728px; top: 930px; width: 260px; height: 330px;
    border-radius: 70% 30% 0 0 / 60% 40% 0 0;
  }
  .leaf-corner--left {
    left: 0; top: 990px; width: 188px; height: 230px;
    border-radius: 0 80% 0 0 / 0 70% 0 0;
  }
  .emblem {
    position: absolute;
    left: 419px;
    width: 249px;
    height: 162px;
    background: radial-gradient(ellipse at center, rgba(119,202,189,0.55), rgba(119,202,189,0.15) 70%, transparent 72%);
  }
  .emblem--top { top: 284px; }
  .emblem--bottom { top: 755px; }
  .title {
    position: absolute;
    left: 176px;
    right: 152px;
    text-align: center;
    line-height: 1;
    white-space: nowrap;
  }
  .title--organic { top: 432px; font-size: 108px; font-weight: 400; letter-spacing: 1px; left: 190px; }
  .title--collagen { top: 546px; font-family: "Comfortaa", sans-serif; font-weight: 700; font-size: 116px; letter-spacing: -2px; left: 190px; }
  .title--powder { top: 670px; font-size: 82px; font-weight: 300; left: 190px; }
  .divider {
    position: absolute;
    left: 468px; top: 950px;
    width: 152px; height: 5px;
    background: var(--forest);
  }
  .support-intro {
    position: absolute;
    left: 176px; right: 152px; top: 998px;
    text-align: center;
    font-size: 28px;
    font-weight: 200;
    padding-left: 10px;
  }
  .benefit-band {
    position: absolute;
    left: 340px; top: 1058px;
    width: 388px; height: 33px;
    background: var(--teal);
    color: var(--forest);
    font-family: "Montserrat", sans-serif;
    font-weight: 800;
    font-size: 18px;
    line-height: 33px;
    text-align: center;
    letter-spacing: 0.2px;
  }
</style>
</head>
<body>
  <main class="label">
    <div class="side-art side-art--left" role="img" aria-label="Cow-spot pattern in teal and forest green above a meadow with grazing cow silhouette and large leaves"></div>
    <div class="side-art side-art--right" role="img" aria-label="Cow-spot pattern in teal and forest green above a green hill with a cow silhouette and large leaves"></div>
    <div class="splash splash--top" role="img" aria-label="Teal liquid splash decoration"></div>
    <div class="splash splash--mid" role="img" aria-label="Small teal splash drop"></div>
    <div class="leaf-corner leaf-corner--right" role="img" aria-label="Large teal leaf with veins"></div>
    <div class="leaf-corner leaf-corner--left" role="img" aria-label="Large teal leaf with veins"></div>

    <div class="emblem emblem--top" role="img" aria-label="Teal three-leaf outline emblem"></div>
    <h1 class="title title--organic">Organic</h1>
    <p class="title title--collagen">Collagen</p>
    <p class="title title--powder">Powder</p>
    <div class="emblem emblem--bottom" role="img" aria-label="Teal three-leaf outline emblem, inverted"></div>

    <div class="divider"></div>
    <p class="support-intro">Provides Natural Support for:</p>
    <p class="benefit-band">HEALTHY NUTRITION AND STAY FIT</p>
  </main>
</body>
</html>
```